Stranded by paperwork book cover

Black book cover with image of man in a white coat with gold bars. Inspiration is the book cover below. The book is about medical corruption and how medical services are now all about the money. Full title:

Stranded by ‘Paperwork’
Why clerks and committees bury your dreams under forms and how to climb out regardless.

5.5 x 8 inches is the size of the book.

I"m trying to upload the image I liked; should be sort of like this
Updates

complete title: Stranded by ‘Paperwork’ Why clerks and committees bury your dreams under forms and how to climb out regardless. I attached a book cover that i liked. I'll try again. 5.5 inches by 8.5 inches cover size.

Target Market(s)

doctors and patients.

Colors

Designer to choose colors to be used in the design.

Requirements
Must have
• black cover

```html
<!DOCTYPE html>
<html lang="en">
<head>
<meta charset="utf-8">
<title>Stranded by ‘Paperwork’ — Book Cover</title>
<link rel="stylesheet" href="https://fonts.googleapis.com/css2?family=Anton&family=Bebas+Neue&display=swap">
<style>
  :root {
    --page-bg: #ffffff;
    --cover-black: #050505;
    --title-red: #e0061a;
    --subtitle-gold: #e8b40c;
    --subtitle-gold-dark: #b88a05;
    --author-white: #f4f4f4;
    --coat-light: #f2f2f2;
    --coat-shade: #bfc3c8;
    --gold-light: #f3d27a;
    --gold-mid: #c99a2e;
    --gold-dark: #5a4210;
  }
  * { margin: 0; padding: 0; box-sizing: border-box; }
  html, body {
    width: 1170px;
    height: 1200px;
    overflow: hidden;
    background: var(--page-bg);
  }
  .stage {
    position: relative;
    width: 1170px;
    height: 1200px;
  }
  .cover {
    position: absolute;
    left: 235px;
    top: 60px;
    width: 700px;
    height: 1080px;
    background: var(--cover-black);
    overflow: hidden;
  }
  .cover-title {
    position: absolute;
    top: 64px;
    left: 0;
    width: 100%;
    text-align: center;
    font-family: "Anton", sans-serif;
    font-size: 112px;
    line-height: 1.0;
    color: var(--title-red);
    text-transform: uppercase;
    letter-spacing: -1px;
    z-index: 3;
  }
  .cover-title span { display: block; }
  .portrait {
    position: absolute;
    left: 150px;
    top: 300px;
    width: 400px;
    height: 540px;
    background: radial-gradient(ellipse at 50% 55%, var(--coat-light) 0%, #dcdfe2 45%, var(--coat-shade) 70%, rgba(5,5,5,0) 100%);
    z-index: 1;
  }
  .subtitle-band {
    position: absolute;
    left: 150px;
    top: 480px;
    width: 470px;
    height: 150px;
    background: var(--cover-black);
    z-index: 2;
  }
  .cover-subtitle {
    position: absolute;
    left: 150px;
    top: 490px;
    width: 470px;
    text-align: center;
    font-family: "Anton", sans-serif;
    font-size: 34px;
    line-height: 1.12;
    text-transform: uppercase;
    background: linear-gradient(180deg, var(--subtitle-gold) 0%, var(--subtitle-gold) 55%, var(--subtitle-gold-dark) 100%);
    -webkit-background-clip: text;
    background-clip: text;
    color: transparent;
    z-index: 3;
  }
  .gold-bars {
    position: absolute;
    left: 130px;
    top: 790px;
    width: 440px;
    height: 170px;
    background: linear-gradient(170deg, var(--gold-light) 0%, var(--gold-mid) 45%, var(--gold-dark) 100%);
    border-radius: 6px;
    z-index: 2;
  }
  .cover-author {
    position: absolute;
    left: 150px;
    top: 972px;
    width: 400px;
    text-align: center;
    font-family: "Bebas Neue", sans-serif;
    font-size: 66px;
    line-height: 1;
    letter-spacing: 3px;
    color: var(--author-white);
    z-index: 3;
  }
</style>
</head>
<body>
  <main class="stage">
    <section class="cover">
      <h1 class="cover-title">
        <span>Stranded by</span>
        <span>‘Paperwork’</span>
      </h1>
      <div class="portrait" role="img" aria-label="Photo of a man in a white lab coat and blue tie with arms crossed, face hidden behind the title"></div>
      <div class="subtitle-band"></div>
      <p class="cover-subtitle">Why clerks and committees bury your dreams under forms and how to climb out regardless</p>
      <div class="gold-bars" role="img" aria-label="Photo of a stack of shiny gold bars"></div>
      <p class="cover-author">Daniel Marsh</p>
    </section>
  </main>
</body>
</html>
```